Bright Meadow Care Partners, LLC

We are private duty home care agency. We provide in-home care for people of all ages. Our kind natured and patient caregivers provide assistance to those who have difficulty with caring for themselves. We already have a logo designed by ArtNestly

```html
<!DOCTYPE html>
<html lang="en">
<head>
<meta charset="utf-8">
<title>Bright Meadow Care Partners, LLC</title>
<link rel="stylesheet" href="https://fonts.googleapis.com/css2?family=Raleway:wght@600;700;800&family=Lato:wght@400;700&display=swap">
<style>
:root{
  --green:#3a9a12;
  --green-deep:#2a8a06;
  --lime:#9bee12;
  --orange:#ff6a00;
  --orange-soft:#fb6a0a;
  --ink:#333333;
  --ink-soft:#555555;
  --grey-bg:#ececec;
  --white:#ffffff;
}
*{margin:0;padding:0;box-sizing:border-box}
html,body{width:1200px;height:3558px;overflow:hidden}
body{position:relative;background:var(--white);font-family:'Lato',sans-serif;color:var(--ink)}
.abs{position:absolute}
.heading{font-family:'Raleway',sans-serif;font-weight:700}
.btn{position:absolute;display:flex;align-items:center;justify-content:center;color:var(--white);font-family:'Raleway',sans-serif;font-weight:700;font-size:18px;letter-spacing:.3px;text-decoration:none}
.btn-orange{background:var(--orange)}
.btn-green{background:var(--green-deep)}
.btn-outline{border:2px solid var(--white);font-size:15px}

/* header */
.brand{left:138px;top:34px;display:flex;align-items:center;gap:10px}
.brand-dot{width:22px;height:22px;border-radius:50%;background:var(--orange)}
.brand-name{font-family:'Raleway',sans-serif;font-weight:800;font-size:24px;color:var(--green);line-height:1.1;width:220px}
.nav{top:48px;font-size:18px;color:#222}
.phone{left:932px;top:44px;font-size:19px;color:#222;display:flex;align-items:center;gap:6px}

/* hero */
.hero-photo{left:0;top:0;width:1200px;height:704px;background:linear-gradient(90deg,#f7f5f2 0%,#f1ece6 35%,#e9dccd 55%,#d9c3ad 75%,#cdb49d 100%)}
.hero-mark{left:331px;top:226px;width:28px;height:28px;border-radius:50%;background:var(--orange)}
.hero-title{left:145px;width:400px;text-align:center;top:294px;font-size:34px;color:var(--green);font-weight:800}
.hero-sub{left:145px;width:400px;text-align:center;top:332px;font-size:27px;color:var(--orange)}
.hero-text{left:165px;width:360px;text-align:center;top:376px;font-size:16px;line-height:24px;color:#333}
.round-arrow{width:62px;height:62px;border-radius:50%;background:rgba(120,120,120,.6);display:flex;align-items:center;justify-content:center}

/* about */
.about-title{left:615px;top:796px;font-size:36px;font-weight:800;color:var(--green)}
.about-title span{color:var(--orange)}
.lead{font-size:17px;line-height:27px;color:var(--ink-soft)}
.body-copy{font-size:15.5px;line-height:27px;color:var(--ink-soft)}

/* services */
.services-title{left:0;width:1200px;text-align:center;top:1294px;font-size:29px;color:var(--white)}
.service-title{font-family:'Raleway',sans-serif;font-weight:700;font-size:19px;line-height:23px;color:var(--white);width:290px}
.service-text{font-size:14px;line-height:23px;color:#ffe2cc;width:300px}
.service-icon{width:114px;height:114px}

/* why */
.why-photo{left:0;top:1810px;width:603px;height:530px;background:linear-gradient(135deg,#e7dccb 0%,#c9b7a0 40%,#a9a4b4 70%,#e8e1e4 100%)}
.why-bg{left:603px;top:1810px;width:597px;height:610px;background:var(--grey-bg)}
.why-title{left:667px;top:1926px;font-size:31px;color:#444}

/* testimonials */
.testi-title{left:0;width:1200px;text-align:center;top:2408px;font-size:27px;font-family:'Raleway',sans-serif;font-weight:600;color:var(--white)}
.quote{left:452px;top:2466px;width:540px;font-size:18px;line-height:32.5px;color:var(--white)}
.qmark{font-family:'Raleway',sans-serif;font-weight:800;font-size:60px;color:var(--white);line-height:1}
.testi-name{left:452px;top:2610px;font-size:17px;font-weight:700;color:var(--white)}

/* blogs */
.blogs-title{left:0;width:1200px;text-align:center;top:2812px;font-size:33px;color:var(--orange);font-weight:700}
.blog-meta{font-size:13px;color:var(--orange)}
.blog-title{font-size:17px;line-height:24px;color:#222;text-transform:uppercase}
.blog-text{font-size:12px;line-height:21px;color:#555}
.learn{font-size:15px;font-weight:700;color:var(--green-deep)}
.thumb{width:128px;height:118px}
.rule{left:635px;width:416px;height:1px;background:#cccccc}

/* footer */
.footer{left:0;top:3407px;width:1200px;height:151px;background:var(--grey-bg);border-top:2px solid #dddddd}
.foot-link{top:3456px;font-size:17px;color:#222}
.social{top:3451px;width:32px;height:32px;border-radius:50%;background:#2f5ea5}
.copy{left:174px;top:3494px;font-size:11.5px;color:#222}
</style>
</head>
<body>

<!-- hero -->
<div class="abs hero-photo" role="img" aria-label="Caregiver listening to an elderly woman's heart with a stethoscope in a bright living room"></div>

<header>
  <div class="abs brand"><span class="brand-dot"></span><span class="brand-name">Bright Meadow Care Partners</span></div>
  <nav>
    <a class="abs nav" style="left:411px">About Us</a>
    <a class="abs nav" style="left:512px">Our Services</a>
    <a class="abs nav" style="left:639px">Blogs</a>
    <a class="abs nav" style="left:711px">Testimonial</a>
    <a class="abs nav" style="left:835px">Contact</a>
  </nav>
  <div class="abs phone">
    <svg width="18" height="18" viewBox="0 0 24 24"><path fill="#2a8a06" d="M6.6 10.8a15.1 15.1 0 0 0 6.6 6.6l2.2-2.2a1 1 0 0 1 1-.25 11.4 11.4 0 0 0 3.6.57 1 1 0 0 1 1 1V20a1 1 0 0 1-1 1A17 17 0 0 1 3 4a1 1 0 0 1 1-1h3.5a1 1 0 0 1 1 1c0 1.25.2 2.45.57 3.57a1 1 0 0 1-.25 1z"/></svg>
    555 014 2290
  </div>
</header>

<section>
  <div class="abs hero-mark"></div>
  <h1 class="abs heading hero-title">LIVE INDEPENDENTLY</h1>
  <h2 class="abs heading hero-sub">IN YOUR OWN HOME</h2>
  <p class="abs hero-text">Lorem ipsum dolor sit amet consectetuer adipiscing elit Nam cursus Morbi</p>
  <a class="btn btn-orange" style="left:239px;top:447px;width:210px;height:47px">GET A FREE CALL</a>
  <div class="abs round-arrow" style="left:55px;top:329px"><svg width="20" height="28" viewBox="0 0 20 28"><path d="M15 3 5 14l10 11" fill="none" stroke="#fff" stroke-width="3"/></svg></div>
  <div class="abs round-arrow" style="left:1074px;top:329px"><svg width="20" height="28" viewBox="0 0 20 28"><path d="M5 3l10 11L5 25" fill="none" stroke="#fff" stroke-width="3"/></svg></div>
</section>

<!-- about -->
<section>
  <svg class="abs" style="left:0;top:0" width="1200" height="1200" viewBox="0 0 1200 1200">
    <circle cx="367" cy="954" r="204" fill="var(--lime)"/>
    <circle cx="378" cy="962" r="196" fill="var(--orange)"/>
  </svg>
  <div class="abs" role="img" aria-label="Smiling senior man with a home care nurse taking notes on the sofa" style="left:190px;top:773px;width:362px;height:362px;border-radius:50%;background:linear-gradient(135deg,#d8c6b4 0%,#b98d7e 40%,#8fa3b6 75%,#dfe4e6 100%)"></div>
  <h2 class="abs heading about-title">ABOUT <span>BRIGHT MEADOW</span></h2>
  <p class="abs lead" style="left:615px;top:862px;width:470px">Pellentesque faucibus Ut accumsan ultricies elit Maecenas at justo id velit placerat molestie</p>
  <p class="abs body-copy" style="left:615px;top:928px;width:470px">Enim iaculis aliquam Mauris nunc quam venenatis nec euismod sit amet egestas placerat est Pellentesque habitant morbi tristique senectus et netus et malesuada fames ac turpis egestas Cras id elit Integer quis urna</p>
  <a class="btn btn-orange" style="left:615px;top:1070px;width:180px;height:47px">LEARN MORE</a>
</section>

<!-- why section base layers -->
<div class="abs why-bg"></div>
<div class="abs why-photo" role="img" aria-label="Nurse checking the blood pressure of a senior woman seated on her bed"></div>

<!-- bands -->
<svg class="abs" style="left:0;top:0" width="1200" height="3558" viewBox="0 0 1200 3558">
  <path d="M560 1228 C850 1245 1080 1300 1200 1348 L1200 1290 Z" fill="var(--lime)"/>
  <path d="M0 1700 C140 1768 300 1800 520 1822 C300 1826 110 1795 0 1772 Z" fill="var(--lime)"/>
  <path d="M0 1220 C360 1210 760 1205 1200 1312 L1200 1808 C900 1828 600 1830 320 1795 C170 1775 60 1748 0 1722 Z" fill="var(--orange-soft)"/>
  <path d="M560 2336 C860 2345 1090 2385 1200 2448 L1200 2398 Z" fill="var(--orange)"/>
  <path d="M0 2655 C110 2715 260 2748 470 2766 C260 2768 90 2735 0 2708 Z" fill="var(--orange)"/>
  <path d="M0 2333 C400 2328 820 2338 1200 2416 L1200 2744 C900 2764 520 2770 260 2732 C130 2714 45 2692 0 2674 Z" fill="var(--green-deep)"/>
</svg>

<!-- services -->
<section>
  <div class="abs" style="left:588px;top:1250px;width:24px;height:24px;border-radius:50%;background:var(--white)"></div>
  <h2 class="abs heading services-title">OUR SERVICES</h2>

  <svg class="abs service-icon" style="left:175px;top:1361px" viewBox="0 0 114 114" role="img" aria-label="Hand washing icon"><path d="M70 4 A55 55 0 1 0 110 60" fill="none" stroke="#fff" stroke-width="3"/><circle cx="57" cy="57" r="26" fill="none" stroke="#fff" stroke-width="2" opacity=".6"/></svg>
  <h3 class="abs service-title" style="left:302px;top:1374px">Help with Personal Hygiene and Care</h3>
  <p class="abs service-text" style="left:302px;top:1432px">Pellentesque faucibus Ut accumsan ultricies elit Maecenas at justo id velit placerat</p>

  <svg class="abs service-icon" style="left:627px;top:1361px" viewBox="0 0 114 114" role="img" aria-label="Plate with cutlery icon"><path d="M70 4 A55 55 0 1 0 110 60" fill="none" stroke="#fff" stroke-width="3"/><circle cx="57" cy="57" r="30" fill="none" stroke="#fff" stroke-width="2"/><circle cx="57" cy="57" r="20" fill="none" stroke="#fff" stroke-width="2"/></svg>
  <h3 class="abs service-title" style="left:753px;top:1374px">Assisting with Meals and Nutrition</h3>
  <p class="abs service-text" style="left:753px;top:1432px">Pellentesque faucibus Ut accumsan ultricies elit Maecenas at justo id velit placerat</p>

  <svg class="abs service-icon" style="left:175px;top:1542px" viewBox="0 0 114 114" role="img" aria-label="Broom and bucket icon"><path d="M70 4 A55 55 0 1 0 110 60" fill="none" stroke="#fff" stroke-width="3"/><path d="M40 80 H84 M50 30 L74 80" fill="none" stroke="#fff" stroke-width="2"/></svg>
  <h3 class="abs service-title" style="left:302px;top:1555px">Home Maintenance and Housekeeping</h3>
  <p class="abs service-text" style="left:302px;top:1613px">Pellentesque faucibus Ut accumsan ultricies elit Maecenas at justo id velit placerat</p>

  <svg class="abs service-icon" style="left:627px;top:1545px" viewBox="0 0 114 114" role="img" aria-label="Pill capsule icon"><path d="M70 4 A55 55 0 1 0 110 60" fill="none" stroke="#fff" stroke-width="3"/><rect x="34" y="38" width="40" height="18" rx="9" transform="rotate(-45 54 47)" fill="none" stroke="#fff" stroke-width="2"/><ellipse cx="72" cy="74" rx="14" ry="7" fill="none" stroke="#fff" stroke-width="2"/></svg>
  <h3 class="abs service-title" style="left:753px;top:1559px">Prescription Medication Management</h3>
  <p class="abs service-text" style="left:753px;top:1617px">Pellentesque faucibus Ut accumsan ultricies elit Maecenas at justo id velit placerat</p>

  <svg class="abs" style="left:98px;top:1503px" width="22" height="36" viewBox="0 0 22 36"><path d="M18 3 4 18l14 15" fill="none" stroke="#fff" stroke-width="3.5"/></svg>
  <svg class="abs" style="left:1062px;top:1503px" width="22" height="36" viewBox="0 0 22 36"><path d="M4 3l14 15L4 33" fill="none" stroke="#fff" stroke-width="3.5"/></svg>

  <a class="btn btn-outline" style="left:486px;top:1716px;width:223px;height:51px">VIEW MORE SERIVCES</a>
</section>

<!-- why -->
<section>
  <h2 class="abs heading why-title">WHY WE ARE</h2>
  <p class="abs lead" style="left:668px;top:1986px;width:470px;line-height:24px">Pellentesque faucibus Ut accumsan ultricies elit Maecenas at justo id velit placerat molestie</p>
  <p class="abs body-copy" style="left:668px;top:2046px;width:470px;line-height:23.5px">Enim iaculis aliquam Mauris nunc quam venenatis nec euismod sit amet egestas placerat est Pellentesque habitant morbi tristique senectus et netus et malesuada fames ac turpis egestas Cras id elit Integer quis urna</p>
  <a class="btn btn-green" style="left:668px;top:2169px;width:170px;height:45px">LEARN MORE</a>
</section>

<!-- testimonials -->
<section>
  <div class="abs" style="left:595px;top:2366px;width:24px;height:24px;border-radius:50%;background:var(--white)"></div>
  <h2 class="abs testi-title">TESTIMONIALS</h2>
  <svg class="abs" style="left:230px;top:2464px" width="184" height="184" viewBox="0 0 184 184">
    <circle cx="90" cy="92" r="89" fill="var(--lime)"/>
    <circle cx="96" cy="94" r="84" fill="var(--orange)"/>
  </svg>
  <div class="abs" role="img" aria-label="Portrait of a smiling senior man" style="left:248px;top:2482px;width:152px;height:152px;border-radius:50%;background:linear-gradient(135deg,#e8e4de 0%,#c9b8a8 50%,#8c9aa6 100%)"></div>
  <span class="abs qmark" style="left:406px;top:2460px">&ldquo;</span>
  <p class="abs quote">Sed ut perspiciatis unde omnis iste natus error sit voluptatem accusantium doloremque laudantium, totam rem aperiam, eaque ipsa quae ab illo inventore veritatis et quasi architecto beatae vitae dicta sunt explicabo.</p>
  <span class="abs qmark" style="left:728px;top:2570px">&rdquo;</span>
  <p class="abs testi-name">DANIEL REYES</p>
  <svg class="abs" style="left:164px;top:2525px" width="22" height="36" viewBox="0 0 22 36"><path d="M18 3 4 18l14 15" fill="none" stroke="#fff" stroke-width="3.5"/></svg>
  <svg class="abs" style="left:1020px;top:2525px" width="22" height="36" viewBox="0 0 22 36"><path d="M4 3l14 15L4 33" fill="none" stroke="#fff" stroke-width="3.5"/></svg>
</section>

<!-- blogs -->
<section>
  <h2 class="abs heading blogs-title">RECENT BLOGS</h2>

  <div class="abs" role="img" aria-label="Caregiver and senior woman laughing together on a sofa" style="left:164px;top:2894px;width:429px;height:244px;background:linear-gradient(135deg,#c7d3de 0%,#d8bfa8 45%,#b0424a 80%,#e2dcd4 100%)"></div>
  <p class="abs blog-meta" style="left:174px;top:3165px">April 12, 2019 &nbsp;|&nbsp; No Comments</p>
  <h3 class="abs blog-title" style="left:174px;top:3189px;width:410px">MAURIS VEL LACUS VITAE FELIS VESTIBULUM VOLUTPAT ETIAM EST NUNC</h3>
  <p class="abs blog-text" style="left:174px;top:3250px;width:400px">Nunc tempus felis vitae urna Vivamus porttitor neque at volutpat rutrum purus nisi eleifend libero a tempus libero lectus</p>
  <a class="abs learn" style="left:176px;top:3305px">Learn More</a>

  <div class="abs thumb" role="img" aria-label="Caregiver with a senior man at home" style="left:635px;top:2896px;background:linear-gradient(135deg,#d9d4cc,#b49680 60%,#8b8f96)"></div>
  <p class="abs blog-meta" style="left:791px;top:2902px">April 08, 2019 &nbsp;|&nbsp; No Comments</p>
  <h3 class="abs blog-title" style="left:791px;top:2924px;width:260px">MAURIS VEL LACUS VITAE FELIS VESTIBULUM VOLUTPAT</h3>
  <a class="abs learn" style="left:791px;top:2985px">Learn More</a>
  <div class="abs rule" style="top:3031px"></div>

  <div class="abs thumb" role="img" aria-label="Nurse serving breakfast to a senior man" style="left:636px;top:3055px;background:linear-gradient(135deg,#e6dfd6,#caa98f 55%,#9b9fa3)"></div>
  <p class="abs blog-meta" style="left:792px;top:3052px">April 06, 2019 &nbsp;|&nbsp; No Comments</p>
  <h3 class="abs blog-title" style="left:792px;top:3073px;width:260px">FUSCE TELLUS SED METUS AUGUE CONVALLIS ET</h3>
  <a class="abs learn" style="left:792px;top:3135px">Learn More</a>
  <div class="abs rule" style="top:3194px"></div>

  <div class="abs thumb" role="img" aria-label="Carer helping a senior in a care home lounge" style="left:637px;top:3215px;background:linear-gradient(135deg,#ddd2c4,#a97d63 55%,#6e5a50)"></div>
  <p class="abs blog-meta" style="left:794px;top:3217px">April 02, 2019 &nbsp;|&nbsp; No Comments</p>
  <h3 class="abs blog-title" style="left:794px;top:3239px;width:260px">PHASELLUS FELIS DOLOR SCELERISQUE A TEMPUS</h3>
  <a class="abs learn" style="left:794px;top:3297px">Learn More</a>
</section>

<!-- footer -->
<footer>
  <div class="abs footer"></div>
  <a class="abs foot-link" style="left:174px">Home</a>
  <a class="abs foot-link" style="left:250px">About Us</a>
  <a class="abs foot-link" style="left:352px">Our Services</a>
  <a class="abs foot-link" style="left:479px">Blogs</a>
  <a class="abs foot-link" style="left:552px">Why Us</a>
  <a class="abs foot-link" style="left:641px">Testimonial</a>
  <a class="abs foot-link" style="left:762px">Contact</a>
  <span class="abs social" style="left:894px"></span>
  <span class="abs social" style="left:933px;background:#3b8fd6"></span>
  <span class="abs social" style="left:970px;background:#3f6b9c"></span>
  <span class="abs social" style="left:1009px;background:#2a64a8"></span>
  <p class="abs copy">&copy; 2019 Company Name &nbsp;All right reserved</p>
</footer>

</body>
</html>
```